Business Card Design for Kidvale (Hires out childrens play areas)

Looking to have a business card designed for a company we just bought. The company rents out childrens play areas.

I have uploaded a couple of examples of the kind of business card style I like. Here are two more examples:

https://quorvastudio.nz/project/bright-romp-branding/
https://imgvaultcdn.com/design_img/8841052/302917/302917_5518203_8841052_b73e19a2_image.jpg

I think a white card will be best due to all the colours in the logo.

Size we require: 3.75" x 2.25" (horizontally orientated) with a 0.125" bleed

Uploaded is two versions of our logo.

Details for the card:
1. My name: Liam Verster
2. Title: Managing Director
3. Phone no: 021 563 417
4. Email: liam@kidvale.co.nz
5. URL: www.kidvale.co.nz
6. Address:
PO Box 318625
Fernlea, Auckland

Let me know if you need anything else.

Target Market(s)

Hospitals, doctors surgeries, bed shops, etc.

Contact Information for Business Card

Details for the card:
1. My name: Liam Verster
3. Phone no: 021 563 417
5. URL: www.kidvale.co.nz
6. Address:
PO Box 318625
Fernlea, Auckland

Requirements
Should not have
• Not too busy.

```html
<!DOCTYPE html>
<html lang="en">
<head>
<meta charset="utf-8">
<title>Kidvale Business Card</title>
<link href="https://fonts.googleapis.com/css2?family=Crimson+Text:ital,wght@0,400;0,600;1,400&display=swap" rel="stylesheet">
<style>
  :root {
    --backdrop: #d2d3d5;
    --card: #ffffff;
    --brand-blue: #1467b0;
    --brand-green: #3db54a;
    --icon-red: #e3232b;
    --icon-green: #3db54a;
    --icon-orange: #f7941d;
  }
  * { margin: 0; padding: 0; box-sizing: border-box; }
  html, body {
    width: 1200px;
    height: 1003px;
    overflow: hidden;
    background: var(--backdrop);
    font-family: "Crimson Text", Georgia, serif;
  }
  .card {
    position: absolute;
    left: 261px;
    width: 682px;
    height: 410px;
    background: var(--card);
  }
  .card--front { top: 68px; }
  .card--back { top: 523px; }

  .wordmark {
    position: absolute;
    display: flex;
    align-items: center;
    color: var(--brand-blue);
    font-weight: 600;
    line-height: 1;
  }
  .card--front .wordmark {
    left: 0; right: 0; top: 0; bottom: 0;
    justify-content: center;
    font-size: 96px;
    gap: 20px;
  }
  .card--back .wordmark {
    left: 62px;
    top: 150px;
    width: 290px;
    height: 180px;
    justify-content: center;
    font-size: 66px;
    gap: 14px;
  }
  .wordmark__dot {
    width: 0.42em;
    height: 0.42em;
    border-radius: 50%;
    background: var(--brand-blue);
  }

  .contact {
    position: absolute;
    left: 405px;
    top: 90px;
    color: var(--brand-blue);
  }
  .contact__name {
    font-size: 43px;
    font-weight: 600;
    line-height: 1;
    letter-spacing: -0.3px;
  }
  .contact__title {
    font-size: 21px;
    font-style: italic;
    color: var(--brand-green);
    line-height: 1;
    margin-top: 6px;
  }
  .contact__address {
    font-size: 20px;
    line-height: 21px;
    margin-top: 24px;
  }
  .contact__list {
    list-style: none;
    margin-top: 18px;
    font-size: 20px;
  }
  .contact__item {
    display: flex;
    align-items: center;
    height: 28px;
  }
  .contact__item + .contact__item { margin-top: 0; }
  .contact__item:last-child { margin-top: 3px; }
  .contact__icon {
    width: 18px;
    height: 18px;
    margin-right: 10px;
    flex: none;
  }
</style>
</head>
<body>
  <section class="card card--front">
    <div class="wordmark"><span class="wordmark__dot"></span>Kidvale</div>
  </section>

  <section class="card card--back">
    <div class="wordmark"><span class="wordmark__dot"></span>Kidvale</div>

    <div class="contact">
      <h1 class="contact__name">Liam Verster</h1>
      <p class="contact__title">Managing Director</p>
      <p class="contact__address">PO Box 318625<br>Fernlea, Auckland</p>
      <ul class="contact__list">
        <li class="contact__item">
          <svg class="contact__icon" viewBox="0 0 24 24" aria-hidden="true">
            <path fill="var(--icon-red)" d="M6.6 2.5c.6-.3 1.3-.1 1.7.5l2 3.2c.3.6.2 1.3-.3 1.7L8.4 9.2c1.2 2.6 3.4 4.8 6 6l1.3-1.6c.4-.5 1.1-.6 1.7-.3l3.2 2c.6.4.8 1.1.5 1.7l-1 2.2c-.4.9-1.4 1.4-2.4 1.2C10.5 18.9 5.1 13.5 3.6 6.3c-.2-1 .3-2 1.2-2.4z"/>
          </svg>
          021 563 417
        </li>
        <li class="contact__item">
          <svg class="contact__icon" viewBox="0 0 24 24" aria-hidden="true">
            <rect x="1" y="5" width="22" height="15" fill="var(--icon-green)"/>
            <path d="M1.5 5.5 12 13.5 22.5 5.5M1.5 19.5 9 12.5M22.5 19.5 15 12.5" fill="none" stroke="#fff" stroke-width="1.6"/>
          </svg>
          liam@kidvale.co.nz
        </li>
        <li class="contact__item">
          <svg class="contact__icon" viewBox="0 0 24 24" aria-hidden="true">
            <path fill="var(--icon-orange)" d="M21 3 4 9.5l6.5 2.5L6 21.5l4 1 3.5-8.5 2.5 6.5z"/>
          </svg>
          www.kidvale.co.nz
        </li>
      </ul>
    </div>
  </section>
</body>
</html>
```